Creating a website for a life changing company (Past Q)

We do need a website for our Coaching and Consulting business we recently launched. We do need it for information purposes and that our clients do have the opportunity to subscribe for packages, programs etc.
We would like to see designs which use the colours blue and yellow (see attachment). The final design should communicate our passion for the potential in people and the benefit (going beyond) for them.
Additional information:
Our company (webpage): Past Q (the C stands for "what people cannot see / imagine now...)
Welcome to Past Q(uarter)
Consulting (R.I.M.) & Coaching (Rise further)
Two pillars:
1) R.I.M. ( Stewardship ascent - Our program - focussing on companies - business orientated)
2) Rise further (Path renewal - Events - focusing on individuals - primarily life changing)
For both of them we offer: Concierge & Past Q+ (This should go as a subscription)
Eventually you can draft this as a rhombus
Industry/Entity Type
Coaching / Consulting
Coding
Coded - Design and coding required
Number of Pages Required
1 page
Font styles to use
Other font styles liked:
- Lato
Requirements
Must have
- Please see attachment (About us / Offers / Calendar function / Links to Instagram and LinkedIn account / mailing list / page for clients
Nice to have
- A banner

```html
<!DOCTYPE html>
<html lang="en">
<head>
<meta charset="utf-8">
<title>Past Q</title>
<link href="https://fonts.googleapis.com/css2?family=Lato:wght@400;700;900&family=Montserrat:wght@500;600;700&display=swap" rel="stylesheet">
<style>
:root{
  --navy:#062b52;
  --navy-2:#0a3159;
  --navy-3:#12375f;
  --panel:#072e57;
  --yellow:#fff200;
  --ink:#0b2d52;
  --white:#ffffff;
  --muted:#b9c3d0;
}
*{margin:0;padding:0;box-sizing:border-box}
html,body{width:1200px;height:2792px;overflow:hidden}
body{position:relative;background:var(--navy);font-family:'Lato',sans-serif;color:var(--yellow)}
.abs{position:absolute}

/* header */
.site-header{left:0;top:0;width:1200px;height:96px;background:var(--navy)}
.brand{left:100px;top:28px;display:flex;align-items:center;gap:14px}
.brand .dash{width:16px;height:2px;background:var(--muted)}
.brand .mark{width:14px;height:14px;border-radius:50%;background:var(--yellow)}
.brand .name{font-weight:900;font-size:22px;color:var(--yellow);letter-spacing:1px}
.main-nav{left:327px;top:38px;display:flex;gap:30px}
.main-nav a{color:var(--yellow);text-decoration:none;font-weight:700;font-size:16px}

/* hero */
.hero{left:0;top:96px;width:1200px;height:625px;background:linear-gradient(90deg,#f4f5f6 0%,#e4e7ea 40%,#9aa3ad 65%,#5d6670 100%)}
.hero-title{left:101px;top:270px;font-size:66px;font-weight:900;color:var(--ink);letter-spacing:-1px}
.hero-text{left:101px;top:358px;font-size:16px;line-height:28px;color:var(--ink)}
.btn{display:flex;align-items:center;justify-content:center;background:var(--yellow);color:var(--ink);font-weight:700;border-radius:20px;text-decoration:none}
.hero-btn{left:101px;top:436px;width:162px;height:38px;font-size:15px}
.dots{left:545px;top:673px;display:flex;gap:15px}
.dots span{width:10px;height:10px;border-radius:50%;background:rgba(255,255,255,.45)}
.dots span.on{background:#fff}

/* intro */
.intro-dots{left:95px;top:807px}
.intro-photo{left:120px;top:831px;width:469px;height:368px;border-radius:14px;background:linear-gradient(120deg,#2a4c6a,#6b7f85 50%,#c99a6e)}
.section-title{display:flex;align-items:center;justify-content:center;gap:20px;font-weight:900;color:var(--yellow)}
.section-title::before,.section-title::after{content:"";width:60px;height:3px;background:var(--yellow)}
.intro-title{left:600px;top:890px;width:546px;font-size:40px}
.intro-sub{left:600px;top:970px;width:546px;text-align:center;font-size:28px}
.intro-tag{left:600px;top:1034px;width:546px;text-align:center;font-size:30px;font-weight:900;line-height:37px}

/* about */
.about{left:0;top:1295px;width:1200px;height:846px;background:var(--navy-2)}
.about-title{left:0;top:1385px;width:1200px;font-size:40px}
.about-text{left:140px;top:1448px;width:920px;text-align:center;font-size:18px;line-height:31px}
.portrait{top:1577px;border-radius:18px}
.portrait-a{left:202px;width:375px;height:376px;background:linear-gradient(160deg,#3b3a35,#1f3552 60%,#d6d4d2)}
.portrait-b{left:612px;width:382px;height:382px;background:linear-gradient(160deg,#3aa6a8,#56664a 55%,#8b8a5a)}
.about-btn{left:475px;top:1997px;width:250px;height:38px;font-size:15px}

/* contact */
.rails{left:101px;top:2066px;width:12px;height:572px;border-left:1px solid #5d7897;border-right:1px solid #5d7897}
.rails::after{content:"";position:absolute;left:4px;top:0;width:1px;height:100%;background:#5d7897}
.contact{left:0;top:2141px;width:1200px;height:651px;background:linear-gradient(180deg,var(--navy-3),#0d3059)}
.kicker{left:150px;top:2260px;font-family:'Montserrat',sans-serif;font-size:22px;font-weight:600;letter-spacing:1px}
.contact-head{left:148px;top:2294px;font-family:'Montserrat',sans-serif;font-size:48px;font-weight:700;line-height:50px}
.contact-list{left:150px;top:2408px;font-family:'Montserrat',sans-serif;font-size:16px;font-weight:500;list-style:none}
.contact-list li{display:flex;gap:8px;line-height:21px;position:absolute;left:0;white-space:nowrap}
.contact-list svg{flex:none;margin-top:2px}
.directions{left:150px;top:2552px;font-family:'Montserrat',sans-serif;font-size:18px;font-weight:700;padding-bottom:3px;border-bottom:2px solid var(--yellow);letter-spacing:.5px}
.socials{left:151px;top:2593px;display:flex;gap:5px}
.socials span{width:48px;height:48px;border-radius:50%;background:var(--yellow)}
.form-panel{left:569px;top:2233px;width:530px;height:374px;border-radius:16px;background:var(--panel)}
.stripes{left:504px;top:2280px}
.form-title{left:619px;top:2268px;font-family:'Montserrat',sans-serif;font-size:22px;font-weight:700;letter-spacing:1px}
.field{background:#fff;border-radius:16px;color:#333;font-family:'Montserrat',sans-serif;font-size:11px;padding:10px 17px}
.f1{left:618px;top:2314px;width:212px;height:38px}
.f2{left:838px;top:2314px;width:212px;height:38px}
.f3{left:618px;top:2361px;width:212px;height:38px}
.f4{left:838px;top:2361px;width:212px;height:38px}
.f5{left:618px;top:2408px;width:432px;height:94px}
.submit{left:619px;top:2517px;width:123px;height:40px;font-family:'Montserrat',sans-serif;font-size:15px}

/* footer */
.footer-rule{left:100px;top:2701px;width:1000px;height:1px;background:#2c4f77}
.footer-nav{left:100px;top:2724px;display:flex;gap:13px;font-family:'Montserrat',sans-serif;font-size:12.5px;font-weight:600;color:#fff}
.footer-nav .sep{color:#7f93aa;font-weight:400}
.copyright{left:100px;top:2760px;font-family:'Montserrat',sans-serif;font-size:13px;color:#a8b4c3}
.chat{left:1071px;top:2718px;width:55px;height:55px;border-radius:50%;background:var(--yellow);display:flex;align-items:center;justify-content:center}
</style>
</head>
<body>

<header class="abs site-header">
  <div class="abs brand"><span class="dash"></span><span class="mark"></span><span class="name">PAST Q</span><span class="dash"></span></div>
  <nav class="abs main-nav">
    <a href="#">Past Q</a><a href="#">About Us</a><a href="#">R.I.M.</a><a href="#">Concierge</a><a href="#">Rise further</a><a href="#">Past Q+</a><a href="#">Testimonials</a><a href="#">Contact Us</a>
  </nav>
</header>

<section class="abs hero" role="img" aria-label="Two colleagues working together at a laptop in a bright office overlooking a city"></section>
<h1 class="abs hero-title">PAST Q</h1>
<p class="abs hero-text">Lorem ipsum dolor sit amet, consectetur adipiscing elit,<br>sed do eiusmod tempor incididunt ut labore</p>
<a class="abs btn hero-btn" href="#">GET STARTED</a>
<svg class="abs" style="left:58px;top:408px" width="24" height="44" viewBox="0 0 24 44"><path d="M22 2 2 22l20 20" fill="none" stroke="#fff" stroke-width="2"/></svg>
<svg class="abs" style="left:1116px;top:408px" width="24" height="44" viewBox="0 0 24 44"><path d="M2 2l20 20L2 42" fill="none" stroke="#fff" stroke-width="2"/></svg>
<div class="abs dots"><span></span><span class="on"></span><span></span><span></span></div>

<svg class="abs intro-dots" width="134" height="134" viewBox="0 0 134 134">
  <defs><pattern id="dotgrid" width="11.8" height="11.8" patternUnits="userSpaceOnUse"><circle cx="3" cy="3" r="2.8" fill="#fff200"/></pattern></defs>
  <rect x="0" y="0" width="134" height="24" fill="url(#dotgrid)"/>
  <rect x="0" y="0" width="24" height="134" fill="url(#dotgrid)"/>
</svg>
<div class="abs intro-photo" role="img" aria-label="Two smiling business partners shaking hands over a laptop"></div>
<h2 class="abs section-title intro-title">PAST Q</h2>
<p class="abs intro-sub">We R.I.M. your company</p>
<p class="abs intro-tag">We ignite the passion in People to<br>unleash their full Potential!</p>

<section class="abs about"></section>
<h2 class="abs section-title about-title">ABOUT US</h2>
<p class="abs about-text">Welocome to Past Q, where passion for igniting People's Potential is in our DNA and brought Us together The journey starts in the Himalayas to Everst Base Camp, where transformation happened for both of them, it was going Past (Q) what they could see, comprehend and imagine</p>
<div class="abs portrait portrait-a" role="img" aria-label="Portrait of the male co-founder in a navy suit"></div>
<div class="abs portrait portrait-b" role="img" aria-label="Portrait of the female co-founder holding a teal umbrella outdoors"></div>
<a class="abs btn about-btn" href="#">LERAN MORE ABOUT US</a>

<section class="abs contact" role="img" aria-label="Faint city building backdrop"></section>
<div class="abs rails"></div>
<p class="abs kicker">GET IN TOUCH</p>
<h2 class="abs contact-head">CONTACT US<br>TODAY.</h2>
<ul class="abs contact-list">
  <li style="top:0"><svg width="14" height="18" viewBox="0 0 14 18"><path d="M7 1a6 6 0 0 0-6 6c0 4.5 6 10 6 10s6-5.5 6-10a6 6 0 0 0-6-6z" fill="#fff200"/><circle cx="7" cy="7" r="2.3" fill="#12375f"/></svg><span>48 Harbor Lane Northfield<br>USA 30417</span></li>
  <li style="top:67px"><svg width="18" height="18" viewBox="0 0 18 18"><path d="M4 1l3 4-2 2c1 2 3 4 5 5l2-2 4 3-2 3C8 16 2 10 1 4z" fill="none" stroke="#fff200" stroke-width="1.6"/></svg><span>(555) 014-2290</span></li>
  <li style="top:108px"><svg width="20" height="14" viewBox="0 0 20 14"><rect x="1" y="1" width="18" height="12" fill="#fff200"/><path d="M1 1l9 7 9-7" fill="none" stroke="#12375f" stroke-width="1.4"/></svg><span>hello@pastq-mail.com</span></li>
</ul>
<p class="abs directions">GET DIRECTIONS</p>
<div class="abs socials" aria-label="Social links"><span></span><span></span><span></span><span></span></div>

<div class="abs form-panel"></div>
<svg class="abs stripes" width="102" height="18" viewBox="0 0 102 18"><path d="M0 2h102M0 9h102M0 16h102" stroke="#fff200" stroke-width="2.4"/></svg>
<p class="abs form-title">REQUEST A FREE CONSULTATION</p>
<div class="abs field f1">First Name</div>
<div class="abs field f2">Last Name</div>
<div class="abs field f3">Email</div>
<div class="abs field f4">Phone</div>
<div class="abs field f5">Message</div>
<a class="abs btn submit" href="#">SUBMIT</a>

<div class="abs footer-rule"></div>
<nav class="abs footer-nav">
  <span>PAST Q</span><span class="sep">/</span><span>ABOUT US</span><span class="sep">/</span><span>R.I.M.</span><span class="sep">/</span><span>CONCIERGE</span><span class="sep">/</span><span>RISE FURTHER</span><span class="sep">/</span><span>PAST Q+</span><span class="sep">/</span><span>TESTIMONIALS</span><span class="sep">/</span><span>CONTACT US</span><span class="sep">/</span>
</nav>
<p class="abs copyright">©Copyright ©2022 Past Q. All Rights Reserved.</p>
<div class="abs chat"><svg width="26" height="24" viewBox="0 0 26 24"><path d="M3 2h20a2 2 0 0 1 2 2v11a2 2 0 0 1-2 2H10l-6 5v-5H3a2 2 0 0 1-2-2V4a2 2 0 0 1 2-2z" fill="#0b2d52"/><circle cx="8" cy="9.5" r="1.6" fill="#fff200"/><circle cx="13" cy="9.5" r="1.6" fill="#fff200"/><circle cx="18" cy="9.5" r="1.6" fill="#fff200"/></svg></div>

</body>
</html>
```